personal one page website

personal one page site. based on details available on www.drleifosterby.com
design needs to show:
- unique background of doctor
- serving high value customer group
- non-profit work
if you would compare the professional life of DrLeifOsterby with other brands:
a car: it would be corvel brisa
a watch: it would be Volmar Reskali
a sport: horse polo
a sports gear company: zuvo
a drink: macha green tea
a city: Tokyo
the visitor of the site should have the following impressions (in chronological order):
1. Beautiful
2. Interesting
3. this person is a good example for others
4. what will be next ?
www.drleifosterby.com
the main colors should be black / white / grey scales. thank you (including photos).
dear all. the site serves information purpose only and is non-commercial (no phone, appointment, twitter ,fb on the site). you can look at it as an 'online-CV'. no link to the company site 'harbenclinic.com'
Dear All,

```html
<!DOCTYPE html>
<html lang="en">
<head>
<meta charset="utf-8">
<title>Doctor Leif A Osterby, PhD</title>
<link rel="stylesheet" href="https://fonts.googleapis.com/css2?family=Oswald:wght@400;500;600&family=Arimo:wght@400;700&family=Noto+Sans+Arabic:wght@400&display=swap">
<style>
:root{
  --ink:#111;
  --black:#000;
  --white:#fff;
  --text:#7a7a7a;
  --text-dark:#444;
  --band:#ececec;
  --rule:#dcdcdc;
  --rule-strong:#e4e4e4;
  --social:#8a8a8a;
}
*{box-sizing:border-box;margin:0;padding:0}
html,body{width:859px;height:1200px;overflow:hidden;background:var(--white)}
body{position:relative;font-family:"Arimo",Arial,sans-serif;color:var(--text)}
.abs{position:absolute}
.heading{font-family:"Oswald",sans-serif;font-weight:600;color:var(--ink);text-transform:uppercase;letter-spacing:.1px;line-height:1.2}

/* header */
.brand{left:112px;top:20px;width:265px;height:69px;background:var(--black);display:flex;align-items:center;justify-content:center;font-family:"Oswald",sans-serif;font-weight:500;font-size:17px;color:var(--white);letter-spacing:.3px}
.social{display:flex;gap:8px}
.social span{width:15px;height:15px;background:var(--social);display:block}
.social--top{left:688px;top:20px}
.main-nav{left:400px;top:58px;display:flex}
.main-nav a{width:72px;height:34px;display:flex;align-items:center;justify-content:center;font-family:"Oswald",sans-serif;font-size:9.5px;color:#555;text-decoration:none;border-right:1px solid var(--rule);text-transform:uppercase}
.main-nav a:last-child{border-right:0}
.main-nav a.is-current{color:var(--ink);font-weight:600}
.header-rule{left:0;top:105px;width:859px;height:4px;background:var(--rule-strong)}

/* slider */
.slider{left:112px;top:118px;width:636px;height:304px;background:linear-gradient(90deg,#6f6a66 0%,#bdb8b2 28%,#d9d2c7 55%,#a59785 80%,#7a6d60 100%)}
.slider-arrow{top:258px}
.slider-caption{left:112px;top:402px;width:636px;text-align:center;font-size:10px;color:var(--white)}

/* intro band */
.intro-band{left:0;top:437px;width:859px;height:194px;background:var(--band)}
.profile{left:112px;top:448px;width:290px}
.profile h1{font-size:17px;margin-bottom:6px}
.credentials{list-style:none}
.credentials li{font-size:9.2px;line-height:19.5px;color:var(--text)}
.tv{left:430px;top:448px;width:318px}
.tv h2{font-size:17px;margin-bottom:6px}
.video{position:relative;width:318px;height:155px;background:linear-gradient(135deg,#d8d8d8 0%,#5a5f66 45%,#2f3338 70%,#9aa0a6 100%)}
.video-bar{position:absolute;left:0;bottom:0;width:100%;height:18px;background:#1b1b1b;display:flex;align-items:center;gap:10px;padding:0 8px;font-size:8px;color:#ccc}
.video-progress{position:absolute;left:0;bottom:18px;width:100%;height:3px;background:#555}

/* gallery */
.gallery-title{left:112px;top:643px;font-size:17px}
.thumbs{left:112px;top:671px;display:flex;gap:5px}
.thumbs div{width:123px;height:88px}
.btn{display:flex;align-items:center;justify-content:center;background:var(--black);color:var(--white);font-family:"Oswald",sans-serif;font-size:9px;text-transform:uppercase;height:20px;width:54px}
.gallery-more{left:694px;top:770px}
.section-rule{left:112px;top:811px;width:636px;height:1px;background:var(--rule)}
.col-rule{left:430px;top:826px;width:1px;height:302px;background:var(--rule)}

/* press column */
.press-item{left:112px;width:299px}
.press-item h3{font-size:17px;margin-bottom:6px}
.press-body{display:flex;gap:8px}
.press-thumb{width:86px;height:57px;flex:none}
.press-text{font-size:9.2px;line-height:12px;color:var(--text)}
.press-text[lang="ar"]{font-family:"Noto Sans Arabic","Arimo",sans-serif;direction:rtl;text-align:right;font-size:8.4px;line-height:12px}
.press-more{position:absolute;right:0}

/* publications */
.pubs{left:450px;top:826px;width:298px}
.pubs h2{font-size:19px;line-height:25px;margin-bottom:10px}
.pub-list{list-style:none}
.pub-list li{font-size:9px;line-height:12px;color:var(--text);height:44px;padding-top:4px;border-bottom:1px solid var(--rule)}
.pubs-more{left:694px;top:1103px}

/* footer */
.footer-rule{left:0;top:1137px;width:859px;height:3px;background:var(--rule-strong)}
.footer-nav{left:112px;top:1146px;display:flex;gap:18px}
.footer-nav a{font-family:"Oswald",sans-serif;font-weight:500;font-size:9.5px;color:var(--ink);text-decoration:none;text-transform:uppercase}
.copyright{left:112px;top:1166px;font-size:7.5px;color:var(--text-dark)}
.social--bottom{left:688px;top:1151px}
</style>
</head>
<body>

<header>
  <div class="abs brand">Doctor Leif A Osterby, PhD</div>
  <div class="abs social social--top" aria-label="Social links"><span></span><span></span><span></span></div>
  <nav class="abs main-nav">
    <a class="is-current" href="#">Home</a>
    <a href="#">About</a>
    <a href="#">Publications</a>
    <a href="#">Gallery</a>
    <a href="#">Contact</a>
  </nav>
  <div class="abs header-rule"></div>
</header>

<section>
  <div class="abs slider" role="img" aria-label="Photo of Dr Osterby in a white coat seated beside a guest in traditional dress"></div>
  <svg class="abs slider-arrow" style="left:116px" width="14" height="22" viewBox="0 0 14 22"><polyline points="11,2 3,11 11,20" fill="none" stroke="#fff" stroke-width="3"/></svg>
  <svg class="abs slider-arrow" style="left:730px" width="14" height="22" viewBox="0 0 14 22"><polyline points="3,2 11,11 3,20" fill="none" stroke="#fff" stroke-width="3"/></svg>
  <div class="abs slider-caption">Description Three</div>
</section>

<section>
  <div class="abs intro-band"></div>
  <div class="abs profile">
    <h1 class="heading">Doctor Leif A Osterby, PhD</h1>
    <ul class="credentials">
      <li>Doctor of Dental Surgery (West-Germany)</li>
      <li>PhD in Orthodontics / Dentofacial Orthopaedics (West-Germany)</li>
      <li>Fachzahnarzt für Kieferorthopädie (Hamburg, Berlin, Frankfurt)</li>
      <li>Specialist in Lingual Orthodontics (DUOL)</li>
      <li>Diplome Universitaire d'Orthodontie Lingual (Lyrac V)</li>
      <li>Aldmoor Alumnus (ABS, 2005)</li>
      <li>Certificate in Oral Implantology (Level 1, 2, 3)</li>
    </ul>
  </div>
  <div class="abs tv">
    <h2 class="heading">Dr Osterby on Creekside TV</h2>
    <div class="video" role="img" aria-label="Video still from a television interview with Dr Osterby">
      <svg style="position:absolute;left:140px;top:55px" width="36" height="26" viewBox="0 0 36 26"><rect width="36" height="26" rx="5" fill="#111"/><polygon points="14,7 24,13 14,19" fill="#fff"/></svg>
      <div class="video-progress"></div>
      <div class="video-bar">
        <svg width="8" height="9" viewBox="0 0 8 9"><polygon points="0,0 8,4.5 0,9" fill="#ddd"/></svg>
        <svg width="10" height="9" viewBox="0 0 10 9"><polygon points="0,3 3,3 6,0 6,9 3,6 0,6" fill="#ddd"/></svg>
        <span>0:00 / 39:40</span>
      </div>
    </div>
  </div>
</section>

<section>
  <h2 class="abs heading gallery-title">Gallery</h2>
  <div class="abs thumbs">
    <div role="img" aria-label="Dr Osterby holding a book" style="background:linear-gradient(135deg,#cfd6da,#7d8890)"></div>
    <div role="img" aria-label="Dr Osterby with children at a charity event" style="background:linear-gradient(135deg,#c9b98a,#6d6a63)"></div>
    <div role="img" aria-label="Dr Osterby receiving an award" style="background:linear-gradient(135deg,#3d5a7a,#b49a72)"></div>
    <div role="img" aria-label="Group photo at an outdoor event" style="background:linear-gradient(180deg,#9ec2dd,#8a8070)"></div>
    <div role="img" aria-label="Dr Osterby with runners at a sports event" style="background:linear-gradient(180deg,#6aa7d6,#4d6a8a)"></div>
  </div>
  <a class="abs btn gallery-more" href="#">More</a>
  <div class="abs section-rule"></div>
  <div class="abs col-rule"></div>
</section>

<section>
  <article class="abs press-item" style="top:826px;height:92px">
    <h3 class="heading">Dr Osterby in Bay Herald</h3>
    <div class="press-body">
      <div class="press-thumb" role="img" aria-label="Newspaper clipping with Dr Osterby" style="background:linear-gradient(135deg,#e8e4dc,#8e8a86)"></div>
      <p class="press-text">Dr Osterby, 38, said it took him one visit to Dubai as a tourist in August 2001 to decide that he wanted to settle down here for the rest of his life.</p>
    </div>
    <a class="btn press-more" href="#" style="top:70px">More</a>
  </article>

  <article class="abs press-item" style="top:936px;height:92px">
    <h3 class="heading">Dr Osterby in Sahil Al Yawm</h3>
    <div class="press-body">
      <div class="press-thumb" role="img" aria-label="Newspaper clipping with Dr Osterby" style="background:linear-gradient(135deg,#dfe6de,#7c8a7e)"></div>
      <p class="press-text" lang="ar">قال طبيب الأسنان الألماني أوستربي إنه قرر الانتقال إلى دبي في عام 2001 بعد زيارته الأولى للمدينة، وإنه يعتزم البقاء فيها والعمل مع مرضاه من دول الخليج وأوروبا.</p>
    </div>
    <a class="btn press-more" href="#" style="top:70px">More</a>
  </article>

  <article class="abs press-item" style="top:1034px;height:92px">
    <h3 class="heading">Dr Osterby's Book from 1993</h3>
    <div class="press-body">
      <div class="press-thumb" role="img" aria-label="Cover of Dr Osterby's 1993 book" style="background:linear-gradient(180deg,#8fb0c8,#d8d2c4)"></div>
      <p class="press-text">Derzeit nicht verfügbar.<br>Ob und wann dieser Artikel wieder vorrätig sein wird, ist unbekannt.</p>
    </div>
    <a class="btn press-more" href="#" style="top:69px">More</a>
  </article>
</section>

<section class="abs pubs">
  <h2 class="heading">Scientific Publications in Journals and on Conferences</h2>
  <ol class="pub-list">
    <li>1. Review of Lingual Practice 2/1999: Self Ligating Brackets in Lingual Orthodontics (with EB Marrenfeld)</li>
    <li>2. Aldmoor School of Dental Medicine 9/1995: Dental Education in Germany</li>
    <li>3. Global Society for Oral Research 3/1999: Material Properties of latex-free intraoral elastics (with EB Marrenfeld)</li>
    <li>4. Northland Association of Orthodontics 5/1999: Tensile strength and elasticity of latex and latex free intraoral elastics (with EB Marrenfeld)</li>
    <li>5. Vereinigung für Kieferorthopädie Nord 9/1999: Der Einfluss der Extraktionsbehandlung auf das Weichteilprofil (by D Varelis with T Lund)</li>
  </ol>
</section>
<a class="abs btn pubs-more" href="#">More</a>

<footer>
  <div class="abs footer-rule"></div>
  <nav class="abs footer-nav">
    <a href="#">Home</a><a href="#">About</a><a href="#">Publications</a><a href="#">Gallery</a><a href="#">Contact</a>
  </nav>
  <p class="abs copyright">© 2014 Doctor Leif A Osterby, PhD. All Rights Reserved.</p>
  <div class="abs social social--bottom" aria-label="Social links"><span></span><span></span><span></span></div>
</footer>

</body>
</html>
```